Business card design for Tolvin Waste

I would like double-sided business cards for myself and my partner that includes our logo and the existing colour scheme. We provide waste and environmental services to customers in the motor-vehicle and engineering industries.

```html
<!DOCTYPE html>
<html lang="en">
<head>
<meta charset="utf-8">
<title>Tolvin Waste – Business Card</title>
<link rel="stylesheet" href="https://fonts.googleapis.com/css2?family=Arimo:wght@400;700&display=swap">
<style>
  :root {
    --page-bg: #141515;
    --card-bg: #1f2020;
    --ink-white: #f2f2f2;
    --ink-grey: #8d8f8f;
    --brand-green: #7cc242;
    --lime: #a6d93a;
    --divider: #cfcfcf;
  }
  * { box-sizing: border-box; margin: 0; padding: 0; }
  html, body {
    width: 1200px; height: 895px; overflow: hidden;
    background: var(--page-bg);
    font-family: "Arimo", Arial, sans-serif;
  }
  .sheet {
    width: 1200px; height: 895px;
    display: flex; flex-direction: column;
    align-items: center; justify-content: center; gap: 40px;
  }
  .card {
    position: relative;
    width: 680px; height: 388px;
    background: var(--card-bg);
    overflow: hidden;
    box-shadow: 0 12px 30px rgba(0,0,0,.5);
  }
  .card__band {
    position: absolute; left: 0; right: 0; bottom: 0; height: 7px;
  }
  .card--front .card__band { background: var(--lime); }
  .card--back .card__band { background: var(--brand-green); }

  .brand {
    display: flex; align-items: center; gap: 14px;
    font-weight: 700; letter-spacing: 2px;
  }
  .brand__dot {
    width: 46px; height: 46px; border-radius: 50%;
  }
  .brand__name { font-size: 36px; line-height: 1; }

  .card--front .brand {
    position: absolute; left: 50%; top: 138px; transform: translateX(-50%);
    white-space: nowrap;
  }
  .card--front .brand__dot { background: var(--ink-grey); }
  .card--front .brand__name { color: var(--ink-grey); }
  .front__url {
    position: absolute; right: 150px; bottom: 52px;
    font-size: 15px; letter-spacing: 1px; color: var(--ink-white);
  }
  .front__url span { color: var(--brand-green); }

  .card--back .brand {
    position: absolute; left: 50%; top: 70px; transform: translateX(-50%);
    white-space: nowrap;
  }
  .card--back .brand__dot { background: var(--brand-green); }
  .card--back .brand__name { color: var(--ink-white); }

  .person {
    position: absolute; right: 370px; top: 210px;
    text-align: right; color: var(--ink-white);
    font-size: 15px; line-height: 1.25;
  }
  .person__name {
    color: var(--brand-green); font-size: 25px; margin-bottom: 4px;
  }
  .divider {
    position: absolute; left: 335px; top: 200px;
    width: 1px; height: 110px; background: var(--divider);
  }
  .contact {
    position: absolute; left: 356px; top: 205px;
    list-style: none; color: var(--ink-white); font-size: 15px;
  }
  .contact li {
    display: flex; align-items: center; gap: 10px; height: 24px;
  }
  .contact svg { width: 13px; height: 13px; fill: var(--ink-white); flex: none; }
  .contact .accent { color: var(--brand-green); }
</style>
</head>
<body>
<main class="sheet">
  <section class="card card--front" aria-label="Card front">
    <div class="brand">
      <span class="brand__dot"></span>
      <span class="brand__name">TOLVIN WASTE</span>
    </div>
    <p class="front__url">www.<span>tolvinwaste</span>.com</p>
    <div class="card__band"></div>
  </section>

  <section class="card card--back" aria-label="Card back">
    <div class="brand">
      <span class="brand__dot"></span>
      <span class="brand__name">TOLVIN WASTE</span>
    </div>

    <div class="person">
      <p class="person__name">Reed Carlton</p>
      <p class="person__title">Managing Partner</p>
      <p class="person__street">512 NW Cedar Ln. Suite 9</p>
      <p class="person__city">Marlow, NY 10422</p>
    </div>

    <div class="divider"></div>

    <ul class="contact">
      <li>
        <svg viewBox="0 0 24 24"><path d="M6.6 10.8a15 15 0 0 0 6.6 6.6l2.2-2.2c.3-.3.7-.4 1-.2 1.1.4 2.3.6 3.6.6.6 0 1 .4 1 1V20c0 .6-.4 1-1 1A17 17 0 0 1 3 4c0-.6.4-1 1-1h3.5c.6 0 1 .4 1 1 0 1.3.2 2.5.6 3.6.1.3 0 .7-.2 1z"/></svg>
        <span>000-000-0000</span>
      </li>
      <li>
        <svg viewBox="0 0 24 24"><path d="M6 2h12v6H6zM3 9h18a1 1 0 0 1 1 1v7h-4v5H6v-5H2v-7a1 1 0 0 1 1-1zm5 6v5h8v-5z"/></svg>
        <span>999-999-9999</span>
      </li>
      <li>
        <svg viewBox="0 0 24 24"><path d="M2 5h20v14H2zm2 2v.5l8 5 8-5V7l-8 5z"/></svg>
        <span>info@<span class="accent">tolvinwaste</span>.com</span>
      </li>
      <li>
        <svg viewBox="0 0 24 24"><path d="M12 2a10 10 0 1 0 0 20 10 10 0 0 0 0-20zm-1 2.1V8H7.3A8 8 0 0 1 11 4.1zm2 0A8 8 0 0 1 16.7 8H13zM4.6 10H11v4H4.6a8 8 0 0 1 0-4zM13 10h6.4a8 8 0 0 1 0 4H13zm-5.7 6H11v3.9A8 8 0 0 1 7.3 16zm5.7 0h3.7a8 8 0 0 1-3.7 3.9z"/></svg>
        <span>www.<span class="accent">tolvinwaste</span>.com</span>
      </li>
    </ul>

    <div class="card__band"></div>
  </section>
</main>
</body>
</html>
```